Brin’s Beauty. Coffee Scrub Skincare

Graphic design for my Coffee Scrub skin care business. Brin’s Beauty. To go on the packaging. Fun with pastel colours, but still clean and professional. See attached photos on similar businesses packaging. I like the “Tala & Wren” font (see attached photo).

Things to write on the packaging: Brin’s Beauty. Recycled Coffee scrub. Coconut and Chocolate. Recycled packaging. Vegan. Not tested on animal. Recycled coffee. Pink Australian clay. 150g 5.29 oz. Made in Australia.

```html
<!DOCTYPE html>
<html lang="en">
<head>
<meta charset="utf-8">
<title>Brin’s Beauty – Recycled Coffee Scrub Label</title>
<link rel="stylesheet" href="https://fonts.googleapis.com/css2?family=Questrial&family=Crimson+Text&family=Arimo&display=swap">
<style>
  :root {
    --canvas: #ffffff;
    --aqua: #9ed9dc;
    --pink: #f4bfd2;
    --pink-deep: #ec9fbc;
    --ink: #1d1d1d;
    --white: #ffffff;
    --flavour-box: #efefef;
    --illustration: #86c5c9;
  }
  * { margin: 0; padding: 0; box-sizing: border-box; }
  html, body { width: 1200px; height: 998px; overflow: hidden; background: var(--canvas); }
  .canvas { position: relative; width: 1200px; height: 998px; }

  .label {
    position: absolute;
    width: 598px;
    height: 814px;
    background: var(--aqua);
    overflow: hidden;
    font-family: "Questrial", sans-serif;
    color: var(--ink);
  }
  .label--front { left: 90px; top: 93px; }
  .label--pouch {
    left: 785px; top: 448px;
    transform: scale(0.574, 0.565);
    transform-origin: top left;
    box-shadow: 6px 8px 10px rgba(0,0,0,0.35);
  }

  .drip { position: absolute; left: 0; top: 0; width: 598px; height: 300px; }
  .seal-line {
    position: absolute; left: 0; right: 0; top: 60px;
    border-top: 2px dashed var(--white);
  }

  .centered { position: absolute; left: 0; width: 598px; text-align: center; white-space: nowrap; }

  .product-type { top: 216px; font-size: 20px; letter-spacing: 0.2px; }
  .brand-name {
    top: 296px; font-size: 66px; color: var(--white);
    letter-spacing: -1px; line-height: 1;
  }
  .flavour {
    position: absolute; left: 75px; top: 390px; width: 447px; height: 57px;
    background: var(--flavour-box);
    font-size: 30px; line-height: 57px; text-align: center;
  }
  .flavour small { font-size: 20px; }

  .claims {
    position: absolute; left: 208px; top: 472px;
    list-style: none;
    font-family: "Crimson Text", serif; font-size: 17px; line-height: 20px;
  }
  .claims li::before {
    content: ""; display: inline-block; width: 6px; height: 8px;
    margin-right: 4px; background: var(--ink);
    border-radius: 50% 50% 50% 50% / 65% 65% 35% 35%;
  }

  .illustration { position: absolute; background: var(--illustration); border-radius: 40%; }
  .illustration--coconut { left: 45px; top: 462px; width: 165px; height: 150px; }
  .illustration--cacao { left: 380px; top: 485px; width: 175px; height: 125px; }

  .vegan { top: 582px; font-size: 28px; }
  .clay { top: 625px; font-size: 38px; letter-spacing: 0.5px; }
  .origin { top: 680px; font-size: 26px; }
  .weight { top: 747px; font-family: "Arimo", sans-serif; font-size: 22px; }
</style>
</head>
<body>
<main class="canvas">

  <section class="label label--front">
    <svg class="drip" viewBox="0 0 598 300" aria-hidden="true">
      <path fill="var(--pink-deep)" d="M0,0H598V205C585,200 572,205 570,222V275C568,298 532,298 530,275V236C528,218 508,218 505,236V258C503,280 470,280 468,258V232C465,214 445,214 442,232V262C440,285 405,285 403,262V228C400,212 380,212 376,228V250C373,268 345,268 342,250V222C338,205 300,205 296,222V238C292,256 262,256 258,238V226C254,208 220,208 216,226V270C213,296 178,296 175,270V232C172,214 145,214 140,232V258C136,278 105,278 102,258V222C98,206 70,206 66,222V240C62,258 30,258 26,238V222C22,212 10,208 0,210Z"/>
      <path fill="var(--pink)" d="M0,0H598V192C585,188 572,192 570,208V262C568,285 532,285 530,262V222C528,204 508,204 505,222V244C503,266 470,266 468,244V218C465,200 445,200 442,218V248C440,271 405,271 403,248V214C400,198 380,198 376,214V236C373,254 345,254 342,236V208C338,191 300,191 296,208V224C292,242 262,242 258,224V212C254,194 220,194 216,212V256C213,282 178,282 175,256V218C172,200 145,200 140,218V244C136,264 105,264 102,244V208C98,192 70,192 66,208V226C62,244 30,244 26,224V208C22,198 10,194 0,196Z"/>
    </svg>
    <p class="centered product-type">RECYCLED COFFEE SCRUB</p>
    <h1 class="centered brand-name">BRIN’S BEAUTY</h1>
    <p class="flavour">COCONUT <small>AND</small> CHOCOLATE</p>
    <div class="illustration illustration--coconut" role="img" aria-label="Line drawing of a halved coconut with palm fronds"></div>
    <ul class="claims">
      <li>Recycled packaging</li>
      <li>Not tested on animal</li>
      <li>Recycled coffee</li>
    </ul>
    <div class="illustration illustration--cacao" role="img" aria-label="Line drawing of a cacao pod with beans and leaves"></div>
    <p class="centered vegan">VEGAN</p>
    <p class="centered clay">PINK AUSTRALIAN CLAY</p>
    <p class="centered origin">MADE IN AUSTRALIA</p>
    <p class="centered weight">150g 5.29 oz</p>
  </section>

  <section class="label label--pouch">
    <svg class="drip" viewBox="0 0 598 300" aria-hidden="true">
      <path fill="var(--pink-deep)" d="M0,0H598V205C585,200 572,205 570,222V275C568,298 532,298 530,275V236C528,218 508,218 505,236V258C503,280 470,280 468,258V232C465,214 445,214 442,232V262C440,285 405,285 403,262V228C400,212 380,212 376,228V250C373,268 345,268 342,250V222C338,205 300,205 296,222V238C292,256 262,256 258,238V226C254,208 220,208 216,226V270C213,296 178,296 175,270V232C172,214 145,214 140,232V258C136,278 105,278 102,258V222C98,206 70,206 66,222V240C62,258 30,258 26,238V222C22,212 10,208 0,210Z"/>
      <path fill="var(--pink)" d="M0,0H598V192C585,188 572,192 570,208V262C568,285 532,285 530,262V222C528,204 508,204 505,222V244C503,266 470,266 468,244V218C465,200 445,200 442,218V248C440,271 405,271 403,248V214C400,198 380,198 376,214V236C373,254 345,254 342,236V208C338,191 300,191 296,208V224C292,242 262,242 258,224V212C254,194 220,194 216,212V256C213,282 178,282 175,256V218C172,200 145,200 140,218V244C136,264 105,264 102,244V208C98,192 70,192 66,208V226C62,244 30,244 26,224V208C22,198 10,194 0,196Z"/>
    </svg>
    <div class="seal-line"></div>
    <p class="centered product-type">RECYCLED COFFEE SCRUB</p>
    <h2 class="centered brand-name">BRIN’S BEAUTY</h2>
    <p class="flavour">COCONUT <small>AND</small> CHOCOLATE</p>
    <div class="illustration illustration--coconut" role="img" aria-label="Line drawing of a halved coconut with palm fronds"></div>
    <ul class="claims">
      <li>Recycled packaging</li>
      <li>Not tested on animal</li>
      <li>Recycled coffee</li>
    </ul>
    <div class="illustration illustration--cacao" role="img" aria-label="Line drawing of a cacao pod with beans and leaves"></div>
    <p class="centered vegan">VEGAN</p>
    <p class="centered clay">PINK AUSTRALIAN CLAY</p>
    <p class="centered origin">MADE IN AUSTRALIA</p>
    <p class="centered weight">150g 5.29 oz</p>
  </section>

</main>
</body>
</html>
```